MBRT Needs Fundraiser Dinner Invite!!

The Marita Brenkoll Foundation, a 501 3(c) non for profit has a yearly fundraiser, with varying themes. Last year it was "cowboys" and "cowgirls"
This year, it is Parlor 88, or 70's disco music. I have uploaded last years invite for reference, some stock photography for inspiration. You are not limited to using the stock photos.

Annual MBRT Fundraiser Dinner
October 13th, 2022
Starts: 6:30pm
RSVP By: September 20th
Place: The Oxmere
Price: $135 per ticket

Target Market(s)

Donors, Business People, Every person

Industry/Entity Type

Non for Profit

Font styles to use
Sans Serif

Colors
0054AA
0677BA
7BADD7
CADEEF
E8F1F8
E54698
E96AAD
F1A4CE
F9D9EA
FCEFF6
6B429C
8869AF
B7A5CE
E3DAEB
F3F0F8

Requirements
Must have
• The invite should be 5x7, be sophisticated as the clientele are mainly business people that come to support the cause. It should be fun and inviting at the same time.

```html
<!DOCTYPE html>
<html lang="en">
<head>
<meta charset="utf-8">
<title>Annual MBRT Fundraiser Dinner</title>
<link href="https://fonts.googleapis.com/css2?family=Bebas+Neue&family=Raleway:ital,wght@0,400;0,600;0,700;1,700&display=swap" rel="stylesheet">
<style>
  :root{
    --backdrop:#d8d8d8;
    --plum-deep:#2a1656;
    --plum:#4a2c80;
    --plum-glow:#6b429c;
    --sky:#cadeef;
    --sky-shadow:#1e1048;
    --ink:#1d1b33;
    --white:#ffffff;
    --pink:#e96aad;
    --pink-hot:#e54698;
    --pink-soft:#f1a4ce;
    --blue:#0677ba;
    --blue-soft:#7badd7;
    --lavender:#8869af;
    --lilac:#b7a5ce;
    --badge:#e3daeb;
    --badge-line:#9a8ab3;
  }
  *{margin:0;padding:0;box-sizing:border-box}
  html,body{width:1200px;height:1000px;overflow:hidden;background:var(--backdrop)}
  .invite{
    position:absolute;left:287px;top:47px;width:635px;height:901px;overflow:hidden;
    background:radial-gradient(ellipse at 50% 45%,var(--plum-glow) 0%,var(--plum) 45%,var(--plum-deep) 100%);
    font-family:'Raleway',sans-serif;color:var(--white);
  }
  .disco-lights{position:absolute;left:0;top:0;width:635px;height:260px}
  .headline{position:absolute;left:0;right:0;text-align:center;font-family:'Raleway',sans-serif}
  .headline--annual{top:224px;font-size:48px;font-weight:400;line-height:56px}
  .headline--event{top:290px;font-size:56px;font-weight:700;font-style:italic;line-height:64px;letter-spacing:-.5px;text-shadow:0 4px 0 rgba(20,10,50,.6)}
  .pill{
    position:absolute;top:369px;width:268px;height:49px;border-radius:10px;
    background:var(--sky);color:var(--ink);
    font-family:'Bebas Neue',sans-serif;font-size:32px;line-height:51px;text-align:center;
    box-shadow:0 5px 0 var(--sky-shadow);
  }
  .pill--date{left:39px}
  .pill--time{left:320px}
  .detail{position:absolute;left:0;right:0;text-align:center;font-size:26px;font-weight:400;line-height:32px}
  .detail strong{font-weight:700}
  .detail--rsvp{top:457px}
  .detail--place{top:506px}
  .price{
    position:absolute;left:0;right:0;top:568px;text-align:center;line-height:80px;
    font-family:'Bebas Neue',sans-serif;font-size:72px;color:var(--pink);letter-spacing:.5px;
  }
  .footer-wave{position:absolute;left:0;top:0;width:635px;height:901px}
  .disco-art{
    position:absolute;left:320px;top:680px;width:200px;height:160px;border-radius:50%;
    background:radial-gradient(circle at 45% 45%,var(--white) 0%,var(--blue-soft) 30%,var(--pink-soft) 55%,rgba(241,164,206,0) 72%);
  }
  .foundation{
    position:absolute;left:60px;top:812px;display:flex;align-items:center;gap:10px;
    font-family:'Raleway',sans-serif;font-weight:600;font-size:19px;line-height:1.15;color:var(--lavender);
  }
  .foundation__dot{width:16px;height:16px;border-radius:50%;background:var(--lavender);flex:none}
  .partner-badge{position:absolute;left:385px;top:803px;width:74px;height:70px}
  .site{position:absolute;left:462px;top:820px;font-weight:700;font-size:25px;color:var(--lavender)}
</style>
</head>
<body>
  <main class="invite">
    <svg class="disco-lights" viewBox="0 0 635 260" role="img" aria-label="Illustrated 70s disco light beams in pink, blue and purple across the top edge">
      <defs>
        <linearGradient id="lightTone" x1="0" y1="0" x2="1" y2="0">
          <stop offset="0" stop-color="var(--pink-hot)"/>
          <stop offset=".3" stop-color="var(--blue)"/>
          <stop offset=".5" stop-color="var(--pink)"/>
          <stop offset=".75" stop-color="var(--blue-soft)"/>
          <stop offset="1" stop-color="var(--pink-soft)"/>
        </linearGradient>
      </defs>
      <path d="M0 0H635V70C600 110 560 160 500 180C440 200 400 170 360 150C320 140 290 170 250 190C230 200 200 205 190 170C180 130 150 150 120 170C90 200 50 240 0 250Z" fill="url(#lightTone)" opacity=".92"/>
    </svg>

    <h1 class="headline headline--annual">Annual MBRT</h1>
    <h2 class="headline headline--event">Fundraiser Dinner</h2>

    <div class="pill pill--date">October 13th, 2022</div>
    <div class="pill pill--time">Starts: 6:30pm</div>

    <p class="detail detail--rsvp"><strong>RSVP By:</strong> September 20th</p>
    <p class="detail detail--place"><strong>Place:</strong> The Oxmere</p>

    <p class="price">Price: $135 per ticket</p>

    <div class="disco-art" role="img" aria-label="Illustrated mirrored disco ball with sparkles"></div>

    <svg class="footer-wave" viewBox="0 0 635 901" aria-hidden="true">
      <path d="M0 735C40 700 110 682 190 712C255 738 280 790 340 800C420 812 540 772 635 770V901H0Z" fill="var(--white)"/>
    </svg>

    <div class="foundation">
      <span class="foundation__dot"></span>
      <span>The Marita Brenkoll<br>Foundation</span>
    </div>

    <svg class="partner-badge" viewBox="0 0 74 70" aria-hidden="true">
      <rect x="2" y="2" width="70" height="66" rx="8" fill="var(--badge)" stroke="var(--badge-line)" stroke-width="2"/>
    </svg>
    <span class="site">MBRT.ORG</span>
  </main>
</body>
</html>
```